Flyer-Design für Apotheke
Zielgruppe
Wir sind eine Apotheke, mit Schwerpunkt Mutter-Kind / Wiegenhafen Apotheke (www.wiegenhafen Apotheke)
Zielgruppe: Wir haben uns zertifiziert und spezialisiert im Bereich Mütter / Kinderwunsch / Stillen / Babys etc. (Siehe Anbei unser aktueller Entwurf Mutter-Kind-Broschüre)
Wir haben zahlreiche Handouts zu spezifischen Themen von der LHTV und unserem Verein Wiegenhafen Apotheken für unser Kunden schon fertig gestellt (siehe ein Beispiel im Anhang, auf dem wir noch unser Logo eingefügt haben).
Die Handouts sind meist 4-seitig A5, im Anhang mit unserem Logo noch versehen.
Zu zwei Themen möchten wir jetzt noch selbst ein Handout erstellen.
1) Fieberthermometer
2) Schnuller
Ziel: 4-6 Seiten, wir wollen es dann bei Druckfuchs drucken lassen.
Zielgruppe: Mütter, die zu uns in die Apotheke kommen und beraten werden (konkret in diesen Beispielen zum Thema Fieberthermometer bzw. Schnuller. Damit sie was mit nach Hause nehmen können, möchten wir die Handouts erstellen.
Texte anbei, Graphische Umsetzung ggf. mit netten Baby/Mütterbildern o.ä. erwünscht
Aufgabenstellung
Einbau Logo Tolvena-Apotheke (siehe Anhang) ähnlich wie auf dem Flyer Ernährung
(als Logo ohne Adresse etc. und irgendwo unter mit Adresse, Telefon etc.)
Logo Wiegenhafen Apotheke DARF NICHT MIT DRAUF

```html
<!DOCTYPE html>
<html lang="de">
<head>
<meta charset="utf-8">
<title>Der Schnuller – ja oder nein? Informationsbroschüre</title>
<link href="https://fonts.googleapis.com/css2?family=Arimo:wght@400;700&display=swap" rel="stylesheet">
<style>
:root{
  --red:#d0101a;
  --ink:#1d1d1f;
  --grey:#4a4a4e;
  --sky:#d7e3f1;
  --sky-soft:#eef3f9;
  --paper:#ffffff;
  --canvas:#ffffff;
  --photo-pink:#e7c9cf;
  --photo-blue:#b9cde4;
}
*{box-sizing:border-box;margin:0;padding:0}
html,body{width:900px;height:1200px;overflow:hidden;background:var(--canvas)}
body{font-family:"Arimo",Arial,sans-serif;color:var(--ink);position:relative}
.spread{position:absolute;left:76px;width:748px;height:530px;display:flex;box-shadow:0 2px 8px rgba(0,0,0,.18)}
.spread--outside{top:44px}
.spread--inside{top:614px}
.page{position:relative;width:374px;height:530px;overflow:hidden;
  background:linear-gradient(180deg,var(--sky) 0%,var(--sky-soft) 22%,var(--paper) 45%,var(--paper) 62%,var(--sky-soft) 85%,var(--sky) 100%)}
.page + .page{border-left:1px solid #c9d3df}
.page-body{position:absolute;left:34px;right:30px}
.section-title{color:var(--red);font-weight:700;font-size:11px;margin-bottom:8px}
.bullets{list-style:none;font-size:9.3px;line-height:1.28}
.bullets li{position:relative;padding-left:14px;margin-bottom:3px}
.bullets li::before{content:"";position:absolute;left:2px;top:4px;width:4px;height:4px;border-radius:50%;background:var(--ink)}
.note{font-size:9.3px;line-height:1.3}
.note strong{font-weight:700}
.brand{display:flex;align-items:center;gap:8px;font-weight:700;font-size:26px;color:var(--ink);line-height:1}
.brand-dot{width:14px;height:14px;border-radius:50%;background:var(--red)}
.contact{font-size:8.6px;line-height:1.3;font-weight:700;margin-top:6px}
.contact .address{border-bottom:1px solid var(--ink);padding-bottom:2px;margin-bottom:3px}
.disclaimer{position:absolute;left:34px;right:30px;bottom:22px;font-size:6.8px;line-height:1.3;color:var(--grey)}
.cover-kicker{position:absolute;left:30px;top:56px;font-size:10.5px}
.cover-title{position:absolute;left:30px;top:104px;color:var(--red);font-weight:700;font-size:29px;letter-spacing:-.3px}
.cover-sub{position:absolute;left:142px;top:138px;font-size:21px;color:var(--grey)}
.pacifier-mark{position:absolute;right:34px;top:14px;width:88px;height:78px;border-radius:40px;background:rgba(255,255,255,.45)}
.photo{position:absolute}
.photo--cover{left:30px;right:0;top:170px;height:180px;background:linear-gradient(135deg,var(--photo-pink),#f2dde0 55%,#c9a8b2)}
.photo--sleep{left:30px;right:34px;top:24px;height:180px;background:linear-gradient(135deg,#e8e2dc,var(--photo-blue) 60%,#8fa8c6)}
.brand-block{position:absolute;left:30px}
.inside-heading{color:var(--red);font-weight:700;font-size:16px}
.inside-heading span{color:var(--grey);font-weight:400}
.lead{font-size:9.3px;line-height:1.3;margin:14px 0 12px}
.label{font-weight:700}
.tip{font-size:9px;line-height:1.3;margin:3px 0 4px}
.tip b{font-weight:700}
.indent{padding-left:14px}
</style>
</head>
<body>

<section class="spread spread--outside">
  <article class="page page--back">
    <div class="page-body" style="top:118px">
      <h3 class="section-title">Wertvolle Tipps beim Umgang mit dem Beruhigungssauger:</h3>
      <ul class="bullets">
        <li>In den ersten 4-6 Wochen möglichst den Gebrauch vermeiden, um die Milchproduktion optimal anlaufen zu lassen</li>
        <li>Schnuller ist kein Ersatz für engen Körperkontakt und Stillen</li>
        <li>Kein Dauergebrauch, nur kurzzeitige Anwendung</li>
        <li>Falls Schnuller beim Schlafen herausfällt, nicht wieder zurück in den Mund schieben</li>
        <li>Schnuller nicht herumliegen lassen, so wird das Kind dazu verleitet</li>
        <li>Sprechen ohne Beruhigungssauger</li>
        <li>Ab dem 2. Lebensjahr mit dem Abgewöhnen beginnen</li>
        <li>Auf hygienischen Umgang achten</li>
      </ul>
      <p class="note" style="margin-top:16px">Bei weiteren Fragen helfen wir Ihnen gerne weiter.<br><strong>Ihr babyfreundliches Team der Tolvena Apotheke Lindenau</strong></p>
    </div>
    <div class="brand-block" style="left:34px;top:372px">
      <div class="brand"><span class="brand-dot"></span>Tolvena Apotheke</div>
      <div class="contact">
        <div class="address">Lindenstraße 12 · 84312 Lindenau</div>
        tel: 07412 / 584930 · fax: 584930-10<br>
        info@tolvena-apotheke.de<br>
        www.tolvena-apotheke.de
      </div>
    </div>
    <p class="disclaimer">Die vorliegenden Informationen wurden mit größtmöglicher Sorgfalt nach dem derzeitigen aktuellen Stand der Wissenschaft zusammengestellt, dennoch übernehmen Verfasser und Herausgeber keine Gewähr. Es besteht kein Anspruch auf Vollständigkeit.</p>
  </article>

  <article class="page page--cover">
    <div class="pacifier-mark" role="img" aria-label="Zarte Umrisszeichnung eines Schnullers"></div>
    <p class="cover-kicker">Informationsbroschüre</p>
    <h1 class="cover-title">Der Schnuller</h1>
    <p class="cover-sub">ja oder nein?</p>
    <div class="photo photo--cover" role="img" aria-label="Foto: Hand reicht einem Baby einen rosa Schnuller"></div>
    <div class="brand-block" style="top:392px">
      <div class="brand"><span class="brand-dot"></span>Tolvena Apotheke</div>
      <div class="contact">
        <div class="address">Lindenstraße 12 · 84312 Lindenau</div>
        tel: 07412 / 584930 · fax: 584930-10<br>
        info@tolvena-apotheke.de<br>
        www.tolvena-apotheke.de
      </div>
    </div>
  </article>
</section>

<section class="spread spread--inside">
  <article class="page page--inner-left">
    <div class="page-body" style="top:62px">
      <h2 class="inside-heading">Der Schnuller <span>– ja oder nein?</span></h2>
      <p class="lead">Der Einsatz von Schnullern wird kontrovers diskutiert.<br>Die Entscheidung, ob Sie Ihrem Kind einen Beruhigungssauger<br>geben oder nicht, liegt bei Ihnen.</p>
      <h3 class="section-title">Das spricht dafür:</h3>
      <ul class="bullets">
        <li>Zur Beruhigung des Säuglings vor allem bei Trennung von Mutter und Kind</li>
      </ul>
      <p class="note"><span class="label">ABER:</span> kein Allheilmittel zur Ruhigstellung</p>
      <ul class="bullets" style="margin-top:4px">
        <li>Schnuller und Daumen als Ersatz für Brust um Saugbedürfnis zu stillen</li>
        <li>Vorteilhafte Auswirkung auf den Saug- und Schluckreflex bei Frühgeborenen</li>
        <li>Protektiver Effekt auf den plötzlichen Kindstod durch regelmäßigen Gebrauch zum Einschlafen</li>
      </ul>
      <h3 class="section-title" style="margin-top:12px">Das spricht dagegen:</h3>
      <ul class="bullets">
        <li>Hungerzeichen des Kindes werden leichter übersehen</li>
        <li>Mögliche verminderte Milchbildung durch zu seltenes Anlegen an der Brust</li>
        <li>Nur Brust passt sich optimal an kindlichen Mund an, auch kiefergerechte Sauger erfüllen Voraussetzungen nicht</li>
        <li>Saugen am Schnuller erfolgt mit anderen Bewegungen als an Brust &gt; mögliche Irritationen beim Trinken</li>
        <li>Zunge liegt nicht in der normalen Ruheposition</li>
        <li>Kann Störungen im Mundraum (Sprechstörungen, Zahn- und Kieferfehlstellungen, etc.) begünstigen</li>
      </ul>
      <p class="note" style="margin-top:8px">Egal ob Sie sich dafür oder dagegen entscheiden, wichtig ist in jedem Falle ein verantwortungsbewusster und achtsamer Einsatz des Schnullers.</p>
    </div>
    <p class="disclaimer">Die vorliegenden Informationen wurden mit größtmöglicher Sorgfalt nach dem derzeitigen aktuellen Stand der Wissenschaft zusammengestellt, dennoch übernehmen Verfasser und Herausgeber keine Gewähr. Es besteht kein Anspruch auf Vollständigkeit.</p>
  </article>

  <article class="page page--inner-right">
    <div class="photo photo--sleep" role="img" aria-label="Foto: schlafendes Baby mit Schnuller, daneben die Mutter"></div>
    <div class="page-body" style="top:224px;left:30px">
      <h3 class="section-title">Anforderungen an den Schnuller:</h3>
      <ul class="bullets">
        <li>Möglichst niedriger Schnullerschaft<br>&gt; Schneidezähne werden beim Wachstum nicht gehindert</li>
        <li>Raumsparendes und angepasstes Lutschteil</li>
        <li>Vermeidung der Entstehung von zu engen oder kleinen Oberkiefern</li>
      </ul>
      <p class="tip"><b>Achtung:</b> Kirschsauger verhindern den Mundschluss, daher nicht empfehlenswert.</p>
      <ul class="bullets">
        <li>Möglichst flexibles, weiches und bewegliches Lutschteil<br>&gt; mehr Raum für die Zunge als Gaumen- und Kieferformer</li>
      </ul>
      <p class="tip"><b>Tipp:</b> Latex ist weicher als Silikon.</p>
      <ul class="bullets">
        <li>Möglichst leichter Schnuller<br>&gt; Keine Überforderung der Lippen- und Zungenmuskulatur</li>
      </ul>
      <p class="tip"><b>Achtung:</b> Schnullerkette erhöht das Gewicht zusätzlich.</p>
      <ul class="bullets">
        <li>Schnuller muss nicht mitwachsen<br>&gt; Brustwarze verändert sich auch nicht, Zunge braucht wachsenden Freiraum für Sprachentwicklung</li>
        <li>Beruhigungssauger sollte keine Geschmacks- und Zusatzstoffe, sowie gesundheitsschädliche Chemikalien enthalten</li>
      </ul>
    </div>
    <p class="disclaimer" style="left:30px">Die vorliegenden Informationen wurden mit größtmöglicher Sorgfalt nach dem derzeitigen aktuellen Stand der Wissenschaft zusammengestellt, dennoch übernehmen Verfasser und Herausgeber keine Gewähr. Es besteht kein Anspruch auf Vollständigkeit.</p>
  </article>
</section>

</body>
</html>
```